Life Coaching business needs a new flyer

We are an Australian business that specialises in Life Coaching, Career Coaching, Health and Wellness Coaching, Yoga and Pilates. We need a A4 double sided flyer that is full colour and folded to DL format. I have attached a couple of designs that I like and some pictures and would like the flyer to be bright yet stylish.

Life Coaching

```html
<!DOCTYPE html>
<html lang="en">
<head>
<meta charset="utf-8">
<title>Clearpath Coaching – DL Brochure</title>
<link href="https://fonts.googleapis.com/css2?family=Oswald:wght@500;700&family=Lato:wght@400;700&display=swap" rel="stylesheet">
<style>
:root{
  --blue:#1f7fc4;
  --blue-dark:#1a5f9c;
  --blue-pale:#dceaf6;
  --green:#5cb531;
  --green-text:#6cbf2e;
  --ink:#333a40;
  --paper:#ffffff;
  --bg:#d9d9d9;
}
*{box-sizing:border-box;margin:0;padding:0}
html,body{width:861px;height:1200px;overflow:hidden;background:var(--bg)}
body{font-family:"Lato",sans-serif;color:var(--ink);position:relative}
.sheet{position:absolute;left:30px;width:800px;height:566px;background:var(--paper);display:flex;box-shadow:0 2px 8px rgba(0,0,0,.18);overflow:hidden}
.sheet--outside{top:20px}
.sheet--inside{top:614px}
.panel{position:relative;width:266.66px;height:100%;overflow:hidden}
.panel + .panel{border-left:1px solid #eceff2}
.photo{position:absolute}
.round{border-radius:50%;border:4px solid #fff;box-shadow:0 0 0 3px var(--blue-pale)}
.heading{font-family:"Oswald",sans-serif;font-weight:700;text-transform:uppercase;line-height:1.08}
.subhead{color:var(--blue);font-weight:700;font-size:9px;margin-bottom:2px}
.copy{font-size:7.4px;line-height:1.45}
.copy p{margin-bottom:6px}
.cite{font-style:italic}
.brand{display:flex;align-items:center;gap:5px;font-family:"Lato",sans-serif;font-weight:700;color:var(--blue);font-size:11px}
.brand__dot{width:14px;height:14px;border-radius:50%;background:var(--green)}
.green-band{position:absolute;left:0;bottom:0;width:533.33px;height:10px;background:var(--green)}

/* outside: testimonials */
.testimonials{background:linear-gradient(#e6f0f9,#fff 22%)}
.testimonials .copy-block{position:absolute;left:20px;top:26px;width:228px}
.testimonials .photo{left:0;bottom:10px;width:100%;height:190px;background:linear-gradient(180deg,#f4f6f8,#d9dfe6 55%,#c7d1db)}

/* outside: contact */
.contact{text-align:center;padding:26px 22px 0}
.contact .intro{font-size:7px;line-height:1.4;margin-bottom:12px}
.contact .heading{color:var(--green-text);font-size:17px}
.contact .heading small{display:block;font-size:11px;margin-top:3px}
.phone{font-size:19px;letter-spacing:.5px;margin:14px 0 4px}
.contact-line{display:flex;align-items:center;justify-content:center;gap:5px;font-size:7px;margin-bottom:3px}
.contact-line svg{width:9px;height:9px}
.contact .photo{position:relative;margin:12px auto 0;width:150px;height:92px;border:5px solid #fff;box-shadow:0 1px 4px rgba(0,0,0,.35);background:linear-gradient(135deg,#5b4a42,#2e2c2d 60%,#6e6e72)}
.offer{margin:22px auto 0;width:210px;border-top:2px solid var(--ink);border-bottom:2px solid var(--ink);padding:5px 0}
.offer .heading{color:var(--ink);font-size:11px}
.offer .heading small{display:block;font-size:8px;font-weight:500}
.contact .brand{justify-content:center;margin-top:26px}

/* outside: cover */
.cover .group{left:0;top:0;width:267px;height:265px;background:linear-gradient(160deg,#7ab8de,#c98a6a 45%,#a3542f 80%);border-bottom-left-radius:140px}
.cover .ring{position:absolute;left:-30px;top:-40px;width:330px;height:330px;border-radius:50%;border:10px solid var(--blue-pale);opacity:.8}
.cover .beach{left:160px;top:140px;width:104px;height:104px;background:linear-gradient(#9dd0f0,#e9f3fa 60%,#c6d8e4)}
.cover .man{left:105px;top:225px;width:106px;height:106px;background:linear-gradient(135deg,#c7d8e4,#e4a79a 55%,#d9897f)}
.cover .brand{position:absolute;left:68px;top:355px}
.cover .title{position:absolute;left:66px;top:385px;color:var(--blue);font-size:29px}

/* inside: questions */
.questions{background:linear-gradient(180deg,#1d5f9e 0%,#2f7ec0 40%,#8fb8d6 62%,#e8eef2 100%)}
.questions .photo{left:0;top:300px;width:100%;height:266px;background:linear-gradient(180deg,#9fb8c9,#c8d3d8 40%,#9aa39c 70%,#6f756d)}
.questions .list{position:absolute;left:18px;top:24px;width:236px;color:#fff;font-size:14.6px}
.questions .list p{margin-bottom:8px}
.questions .brand{position:absolute;left:14px;bottom:14px;background:#fff;padding:6px 10px;border-radius:3px;font-size:10px}

/* inside: services */
.services{padding:22px 18px 0 18px}
.services .block{margin-bottom:9px}
.services .photo{left:0;bottom:0;width:100%;height:128px;background:linear-gradient(180deg,#9cc7e4,#bcd7e8 40%,#8db15a 62%,#6f9a3f)}

/* inside: help */
.help .arc{position:absolute;left:-40px;top:-120px;width:360px;height:300px;border-radius:50%;border:12px solid var(--blue);border-top-color:transparent;border-left-color:transparent;opacity:.9}
.help .family{left:22px;top:30px;width:140px;height:140px;background:linear-gradient(135deg,#f1c36a,#e39b5e 50%,#c3714a)}
.help .boat{left:150px;top:6px;width:96px;height:96px;background:linear-gradient(#7fb0d8,#dfe8ee 60%,#5c7b93)}
.help .car{left:160px;top:108px;width:72px;height:72px;background:linear-gradient(#8ec6ea,#e9a7b7 60%,#d06f86)}
.help .text{position:absolute;left:20px;top:196px;width:232px}
.ticks{list-style:none;font-size:7.4px;line-height:1.5;margin:2px 0 9px}
.ticks li{display:flex;align-items:center;gap:4px}
.ticks svg{width:7px;height:7px;flex:none}
.help .footer-band{position:absolute;left:0;bottom:0;width:100%;height:70px;background:linear-gradient(180deg,#fff,#cfe2f2)}
.copy--lead{font-weight:700;margin-top:6px}
.copy--spaced{margin-bottom:9px}
</style>
</head>
<body>

<section class="sheet sheet--outside" aria-label="Brochure outside">
  <article class="panel testimonials">
    <div class="copy-block">
      <h3 class="subhead">Happy Clients Testimonials ☺</h3>
      <div class="copy">
        <p>"I have lost 10 kilos and now have the energy to play with my kids. Thanks Mara for your support, guidance and helping me get rid of my limiting beliefs. I feel I can achieve anything now! The sky's the limit" <span class="cite">-Tessa, Mosman</span></p>
        <p>"I had always wanted to start up own café however every time it came to putting it into practice I would procrastinate and not achieve anything. I became overwhelmed with the whole process and never achieved anything. Mara put it into bite sized chunks and helped me to set small achievable goals. I am now a happy café owner." <span class="cite">-Priya, Double Bay</span></p>
        <p>"Mara has helped to change my life around in all aspects. I would have been lost without her. Thanks Mara for your professionalism, support and guidance." <span class="cite">-Elena, Cremorne</span></p>
        <p>"I was so busy with kids, work, and my husband I lost who I was. Mara has helped me find the person I am again." <span class="cite">-Hannah, Chatswood</span></p>
        <p>"When I started with Coach Mara, I didn't know anything about coaching. I called her because she helped a friend of mine make a career change that was a perfect fit for her. I had the opportunity to make a change too and did not know where to start. I am now in a job that I love. I would recommend Mara to everyone." <span class="cite">-Owen, Texas America</span></p>
      </div>
    </div>
    <div class="photo" role="img" aria-label="Photo of three smiling people celebrating with raised fists"></div>
  </article>

  <article class="panel contact">
    <p class="intro">Clearpath Coaching &amp; Meditation Centre is a professional service that can help you achieve the goals that you are looking for in Life Coaching, Meditation, and Yoga/Pilates.</p>
    <h2 class="heading">If you are ready to take your life to the next level and would like to know more,<small>please contact us.</small></h2>
    <p class="phone">02 5550 1834</p>
    <p class="contact-line"><svg viewBox="0 0 10 10"><rect x="0.5" y="2" width="9" height="6" fill="none" stroke="#333" stroke-width="1"/><path d="M0.5 2 5 5.5 9.5 2" fill="none" stroke="#333" stroke-width="1"/></svg>: info@clearpathcoaching.com.au</p>
    <p class="contact-line"><svg viewBox="0 0 10 10"><circle cx="5" cy="5" r="4.3" fill="none" stroke="#333" stroke-width="1"/><path d="M0.7 5h8.6M5 .7c-2 2.5-2 6 0 8.6M5 .7c2 2.5 2 6 0 8.6" fill="none" stroke="#333" stroke-width=".8"/></svg>: www.clearpathcoaching.com.au</p>
    <div class="photo" role="img" aria-label="Framed portrait photo of the two coaches"></div>
    <div class="offer">
      <p class="heading">Free introductory life coaching phone/video session - 20 mins<small>(to see if coaching is right for you)</small></p>
    </div>
    <div class="brand"><span class="brand__dot"></span>Clearpath Coaching</div>
  </article>

  <article class="panel cover">
    <div class="ring"></div>
    <div class="photo group" role="img" aria-label="Photo of a group of happy young friends"></div>
    <div class="photo round beach" role="img" aria-label="Photo of a woman stretching on a beach"></div>
    <div class="photo round man" role="img" aria-label="Photo of a smiling man in a pink shirt"></div>
    <div class="brand"><span class="brand__dot"></span>Clearpath Coaching</div>
    <h1 class="heading title">Life Coaching<br>Meditation<br>Yoga/Pilates</h1>
  </article>
  <div class="green-band"></div>
</section>

<section class="sheet sheet--inside" aria-label="Brochure inside">
  <article class="panel questions">
    <div class="photo" role="img" aria-label="Photo of a hiker with a red backpack sitting above a mountain lake"></div>
    <div class="list heading">
      <p>Are you looking at making changes this year?</p>
      <p>Are you stuck in a rut or at a crossroad in your life?</p>
      <p>Are you wanting to lose weight but can't get motivated?</p>
      <p>Do you have ongoing problems with your career, relationships, or just life itself?</p>
      <p>Life coaching is the answer</p>
    </div>
    <div class="brand"><span class="brand__dot"></span>Clearpath Coaching</div>
  </article>

  <article class="panel services">
    <div class="block">
      <h3 class="subhead">Clearpath Coaching &amp; Meditation Centre</h3>
      <div class="copy">
        <p>Our mission is to help you become the best possible person you can be. Mentally, physically, and spiritually.</p>
        <p>We offer highly qualified and compassionate trainers/coaches for Life Coaching, Meditation, Yoga and Pilates.</p>
        <p>They will guide and motivate you every step of the way to achieve all your dreams and goals.</p>
        <p>They will make you be the best you can be ☺</p>
      </div>
    </div>
    <div class="block">
      <h3 class="subhead">Life Coaching</h3>
      <div class="copy">
        <p>Your Life Coach will give you the confidence and the ability to move forward in a positive manner in all areas of your life where you crave change.</p>
        <p>Life Coaching is about breaking down the barriers preventing this change from happening, and creating the ideal environment for positive action to take place. It is a holistic approach, which looks at the present and sets goals for a totally successful future.</p>
      </div>
    </div>
    <div class="block">
      <h3 class="subhead">Career Coaching</h3>
      <div class="copy"><p>Are you at a crossroads in your career and at a loss about what to do next? Do you want your work to be in alignment with the authentic you? It can be difficult to assess career options, goals, and strategies, and have the confidence to implement changes on your own. With the right coaching support, you will gain the clarity that you need to take control and have a fulfilling and rewarding career.</p></div>
    </div>
    <div class="block">
      <h3 class="subhead">Wellness Coaching</h3>
      <div class="copy"><p>Health and wellness coaches help their clients find the motivation and tools to achieve their health and wellness goals, working with the client to examine and improve the psychological framework that supports those goals.</p></div>
    </div>
    <div class="photo" role="img" aria-label="Photo of a group meditating on yoga mats outdoors"></div>
  </article>

  <article class="panel help">
    <div class="arc"></div>
    <div class="photo round boat" role="img" aria-label="Photo of an older couple on a boat"></div>
    <div class="photo round family" role="img" aria-label="Photo of a mother hugging her daughter in sunlight"></div>
    <div class="photo round car" role="img" aria-label="Photo of a girl cheering in a convertible"></div>
    <div class="footer-band"></div>
    <div class="text">
      <h3 class="subhead">Why Would I Need Help?</h3>
      <p class="copy">Coaching is for anyone who wants to make lasting changes in their life.</p>
      <p class="copy copy--lead">Coaching can assist with such issues as:</p>
      <ul class="ticks">
        <li><svg viewBox="0 0 8 8"><path d="M1 4.2 3 6.2 7 1.5" fill="none" stroke="#5cb531" stroke-width="1.4"/></svg>Creating a better work- life balance</li>
        <li><svg viewBox="0 0 8 8"><path d="M1 4.2 3 6.2 7 1.5" fill="none" stroke="#5cb531" stroke-width="1.4"/></svg>Resolving relationship issues</li>
        <li><svg viewBox="0 0 8 8"><path d="M1 4.2 3 6.2 7 1.5" fill="none" stroke="#5cb531" stroke-width="1.4"/></svg>Career guidance</li>
        <li><svg viewBox="0 0 8 8"><path d="M1 4.2 3 6.2 7 1.5" fill="none" stroke="#5cb531" stroke-width="1.4"/></svg>Stress management</li>
        <li><svg viewBox="0 0 8 8"><path d="M1 4.2 3 6.2 7 1.5" fill="none" stroke="#5cb531" stroke-width="1.4"/></svg>Weight loss and fitness</li>
        <li><svg viewBox="0 0 8 8"><path d="M1 4.2 3 6.2 7 1.5" fill="none" stroke="#5cb531" stroke-width="1.4"/></svg>Motivation and goal setting</li>
        <li><svg viewBox="0 0 8 8"><path d="M1 4.2 3 6.2 7 1.5" fill="none" stroke="#5cb531" stroke-width="1.4"/></svg>Boosting your self esteem</li>
        <li><svg viewBox="0 0 8 8"><path d="M1 4.2 3 6.2 7 1.5" fill="none" stroke="#5cb531" stroke-width="1.4"/></svg>Overcoming negative emotions and thoughts</li>
        <li><svg viewBox="0 0 8 8"><path d="M1 4.2 3 6.2 7 1.5" fill="none" stroke="#5cb531" stroke-width="1.4"/></svg>Better time management</li>
      </ul>
      <h3 class="subhead">Meditation</h3>
      <p class="copy copy--spaced">We specialise in teaching meditation from beginners to advanced and teach a variety of techniques for stress reduction, peace of mind, stillness, and clarity.</p>
      <h3 class="subhead">Yoga/Pilates</h3>
      <p class="copy">Your highly qualified and experienced Yoga or Pilates instructor will come to you and create a fun and varied workout based on what you enjoy and what your goals are.</p>
    </div>
  </article>
</section>

</body>
</html>
```